Im open to ideas.. I was thinking on my business cards aswell as my logo. a place for my name. email. phone number and abn..

ive attched a file with my business logo. which i dont love the colours.. i was think a dark background with charcoal letters so something along those colour schumes but im open to ideas..

Business

BRL Constructions

```html
<!DOCTYPE html>
<html lang="en">
<head>
<meta charset="utf-8">
<title>BRL Constructions – Business Card</title>
<link href="https://fonts.googleapis.com/css2?family=Source+Sans+3:wght@400;600;700&display=swap" rel="stylesheet">
<style>
  :root {
    --stage: #000000;
    --front-top: #7c7c7c;
    --front-bottom: #585858;
    --back-top: #ababab;
    --back-bottom: #8c8c8c;
    --ink-white: #ffffff;
    --ink-soft: #e6e6e6;
    --ink-muted: #c9c9c9;
    --name-grey: #cfcfcf;
    --divider: #9a9a9a;
  }
  * { margin: 0; padding: 0; box-sizing: border-box; }
  html, body {
    width: 1200px; height: 900px; overflow: hidden;
    background: var(--stage);
    font-family: "Source Sans 3", "Myriad Pro", Arial, sans-serif;
  }
  .stage { position: relative; width: 1200px; height: 900px; }

  .card { position: absolute; overflow: hidden; }
  .card-front {
    left: 116px; top: 275px; width: 477px; height: 293px;
    border-radius: 3px 44px 3px 44px;
    background: linear-gradient(180deg, var(--front-top), var(--front-bottom));
  }
  .card-back {
    left: 622px; top: 276px; width: 477px; height: 292px;
    border-radius: 44px 3px 44px 3px;
    background: linear-gradient(180deg, var(--back-top), var(--back-bottom));
  }

  .wordmark { position: absolute; color: var(--ink-white); font-weight: 700; text-align: center; line-height: 1; }
  .wordmark .primary { display: block; letter-spacing: 2px; }
  .wordmark .secondary { display: block; letter-spacing: 0.42em; }

  .card-front .wordmark { left: 38px; top: 48px; width: 236px; }
  .card-front .wordmark .primary { font-size: 56px; }
  .card-front .wordmark .secondary { font-size: 11px; margin-top: 6px; }

  .card-back .wordmark { left: 62px; top: 82px; width: 353px; }
  .card-back .wordmark .primary { font-size: 86px; }
  .card-back .wordmark .secondary { font-size: 15px; margin-top: 10px; }

  .abn { position: absolute; left: 50px; top: 170px; font-size: 13px; color: var(--ink-muted); }
  .abn strong { color: var(--ink-white); font-weight: 700; }

  .holder { position: absolute; right: 19px; top: 151px; text-align: right; }
  .holder-name { font-size: 17px; font-weight: 600; color: var(--name-grey); }
  .holder-role { font-size: 13px; color: var(--ink-white); margin-top: 1px; }

  .divider { position: absolute; left: 0; top: 197px; width: 100%; height: 1px; background: var(--divider); }

  .contacts { position: absolute; left: 50px; top: 211px; list-style: none; }
  .contacts li { display: flex; align-items: center; height: 20px; font-size: 13px; color: var(--ink-soft); }
  .contacts svg { width: 9px; height: 9px; margin-right: 7px; fill: var(--ink-muted); }
</style>
</head>
<body>
<main class="stage">
  <section class="card card-front">
    <div class="wordmark">
      <span class="primary">BRL</span>
      <span class="secondary">CONSTRUCTIONS</span>
    </div>
    <p class="abn">ABN NO: <strong>12345</strong></p>
    <div class="holder">
      <p class="holder-name">Daniel Hayes</p>
      <p class="holder-role">Managing Director</p>
    </div>
    <div class="divider"></div>
    <ul class="contacts">
      <li><svg viewBox="0 0 10 10"><path d="M2 0.5 L3.6 2.6 L2.8 3.6 Q3.8 5.8 6.2 7 L7.3 6.2 L9.5 7.8 L8.4 9.5 Q3.5 9 0.5 2 Z"/></svg>(041)-555-0192</li>
      <li><svg viewBox="0 0 10 10"><path d="M0 2 H10 V8.5 H0 Z M0.8 2.6 L5 5.6 L9.2 2.6 V3.4 L5 6.4 L0.8 3.4 Z" fill-rule="evenodd"/></svg>info@brlbuild.com</li>
      <li><svg viewBox="0 0 10 10"><circle cx="5" cy="5" r="4.6"/></svg>www.brlbuild.com</li>
    </ul>
  </section>

  <section class="card card-back">
    <div class="wordmark">
      <span class="primary">BRL</span>
      <span class="secondary">CONSTRUCTIONS</span>
    </div>
  </section>
</main>
</body>
</html>
```